Pre-drywall Construction postcard mailer

Need a 2-sided postcard to be mailed to real estate agents advertising Pre-drywall Inspections, 5.5 X 8.5 oversized postcard with $25 off the inspection fee. KVO Partners is a home inspection company in Atlanta.

Key words: "New Construction is on the Rise! KVO Inspectors are PLT (code) certified and Fully Insured. Protect your clients with a Pre-drywall inspection."
" $25 coupon for your next Pre-drywall inspection. Mention coupon when booking the Inspection. "
Include a phrase that says, "Once the drywall is hung, hidden problems cannot be seen." Tom Hargrove, Owner KVO

404.555.0187 www.the KVO path.example

Colors: dark green, aqua, lite greens (Go to website to see colors)

Target Market(s)

Real estate agents in SE United States

Industry/Entity Type

Home Inspection

Requirements
Must have
• Our logo (See website) and everything that is in the Task Description. Large one on front and small one by return address.
• Return address for mailer side: 2871 Millbrook Lane, Suite 340 Buford, GA 30519
• Company name: Dwelling Examiners of Meridian, dba KVO Partners
• Ph. # 404.555.0187 www.theKVOpath.example
• Hours: M - F 8:00AM-8PM Sat. 10AM-2PM
• Need illustration of a home under construction-framework only

```html
<!DOCTYPE html>
<html lang="en">
<head>
<meta charset="UTF-8">
<title>KVO Partners – Pre-drywall Inspection Postcard</title>
<link rel="stylesheet" href="https://fonts.googleapis.com/css2?family=Cormorant+Garamond:ital,wght@1,600;1,700&family=Tinos:ital,wght@0,400;0,700;1,400;1,700&family=Carlito:wght@400;700&display=swap">
<style>
  :root {
    --paper: #ffffff;
    --lime-top: #9fd86a;
    --lime-fade: #e3f3d2;
    --quote-navy: #1f3f7a;
    --band-green: #12a84a;
    --deep-green: #0b6b33;
    --band-text: #ffffff;
    --aqua: #2fb8d4;
    --steel-blue: #4a7fc6;
    --aqua-glow: #bfefff;
    --ink: #000000;
    --muted-ink: #2b2b2b;
  }

  * { margin: 0; padding: 0; box-sizing: border-box; }

  html, body {
    width: 1200px;
    height: 776px;
    overflow: hidden;
    background: var(--paper);
  }

  .postcard {
    position: relative;
    width: 1200px;
    height: 776px;
    background: var(--paper);
  }

  .front-panel {
    position: absolute;
    left: 0;
    top: 0;
    width: 651px;
    height: 686px;
    background: linear-gradient(to bottom, var(--lime-top) 0px, var(--lime-fade) 110px, var(--paper) 165px);
  }

  .headline-quote {
    position: absolute;
    left: 58px;
    top: 30px;
    width: 560px;
    font-family: "Cormorant Garamond", "Times New Roman", serif;
    font-style: italic;
    font-weight: 700;
    font-size: 39px;
    line-height: 56px;
    color: var(--quote-navy);
  }

  .construction-illustration {
    position: absolute;
    left: 0;
    top: 150px;
    width: 640px;
    height: 442px;
    background:
      radial-gradient(ellipse 30% 35% at 40% 45%, rgba(191,239,255,0.9) 0%, rgba(191,239,255,0) 100%),
      radial-gradient(ellipse 60% 55% at 30% 45%, rgba(74,127,198,0.45) 0%, rgba(47,184,212,0.25) 60%, rgba(255,255,255,0) 100%),
      var(--paper);
  }

  .offer-band {
    position: absolute;
    left: 0;
    top: 595px;
    width: 651px;
    height: 91px;
    background: var(--band-green);
    padding: 9px 0 0 13px;
    font-family: "Tinos", "Times New Roman", serif;
    font-style: italic;
    font-size: 24.5px;
    line-height: 31px;
    color: var(--band-text);
  }

  .coupon {
    position: absolute;
    left: 13px;
    top: 698px;
    width: 625px;
    height: 66px;
    border: 2px dashed var(--deep-green);
    padding: 6px 12px;
    font-family: "Tinos", "Times New Roman", serif;
    color: var(--deep-green);
    font-size: 17px;
    line-height: 25px;
  }

  .coupon-amount {
    font-weight: 700;
    font-size: 20px;
  }

  .return-address {
    position: absolute;
    left: 690px;
    top: 52px;
    width: 280px;
    font-family: "Carlito", "Calibri", sans-serif;
    font-style: normal;
    font-size: 15px;
    line-height: 21px;
    color: var(--muted-ink);
  }

  .brand-mark {
    display: flex;
    align-items: center;
    gap: 8px;
    margin-bottom: 4px;
    font-weight: 700;
    font-size: 20px;
    line-height: 24px;
    color: var(--deep-green);
  }

  .brand-square {
    width: 14px;
    height: 14px;
    background: var(--aqua);
  }

  .stamp-box {
    position: absolute;
    left: 988px;
    top: 58px;
    width: 141px;
    height: 158px;
    border: 2px solid var(--ink);
  }

  .mailing-address {
    position: absolute;
    left: 793px;
    top: 458px;
    font-family: "Carlito", "Calibri", sans-serif;
    font-style: normal;
    font-size: 22px;
    line-height: 31px;
    color: var(--ink);
  }

  .owner-signoff {
    position: absolute;
    left: 793px;
    top: 700px;
    font-family: "Tinos", "Times New Roman", serif;
    font-style: italic;
    font-size: 17px;
    line-height: 24px;
    color: var(--quote-navy);
  }
</style>
</head>
<body>
  <main class="postcard">
    <section class="front-panel">
      <p class="headline-quote">“Once the drywall is hung, hidden problems cannot be seen.”</p>
      <div class="construction-illustration" role="img" aria-label="Illustration of a blue house frame under construction with a ladder, stacked drywall sheets and pipes"></div>
      <p class="offer-band">KVO Inspectors are PLT (code) certified and Fully Insured.<br>Protect your clients with a Pre-drywall inspection.</p>
    </section>

    <p class="coupon"><span class="coupon-amount">$25 coupon</span> for your next Pre-drywall inspection.<br>Mention coupon when booking the Inspection.</p>

    <address class="return-address">
      <span class="brand-mark"><span class="brand-square"></span>KVO Partners</span>
      Dwelling Examiners of Meridian, dba KVO Partners<br>
      2871 Millbrook Lane, Suite 340<br>
      Buford, GA 30519<br>
      404.555.0187 · www.theKVOpath.example<br>
      Hours: M - F 8:00AM-8PM Sat. 10AM-2PM
    </address>

    <div class="stamp-box" aria-label="Stamp area"></div>

    <address class="mailing-address">
      Address :<br>
      XXXXXXXXXXXXXXXXX<br>
      XXXXXXXXXXXXXXXXX<br>
      XXXXXX
    </address>

    <p class="owner-signoff">Tom Hargrove, Owner KVO</p>
  </main>
</body>
</html>
```